Harbourlight Campus Lodgings needs a business card design

Hi Guys,

We are a Student Accommodation company in Australia. We already have a logo which I will submit.

I will require the design of the business cards from you.

I am after something that looks clean, modern and that people feel interested and actually want to contact us.

We would like to see designs that are innovative.

On the business cards I will require to have:

Employee Name
Position
Phone number
Email
Facebook page

I hope you can help me with this project guys as I have heard really good things from you.

```html
<!DOCTYPE html>
<html lang="en">
<head>
<meta charset="utf-8">
<title>Harbourlight Campus Lodgings – Business Card</title>
<link rel="stylesheet" href="https://fonts.googleapis.com/css2?family=Open+Sans:wght@400;600;700&family=Arimo:wght@400&display=swap">
<style>
  :root {
    --green: #0b8c46;
    --yellow: #f7bd35;
    --white: #ffffff;
    --backdrop: #efe9e0;
    --edge: #d4cfc6;
  }
  * { margin: 0; padding: 0; box-sizing: border-box; }
  html, body { width: 1200px; height: 765px; overflow: hidden; }
  body {
    position: relative;
    background: var(--backdrop);
    font-family: "Open Sans", Arial, sans-serif;
  }
  .card {
    position: absolute;
    width: 597px;
    height: 341px;
    background: var(--white);
    border: 1px solid var(--edge);
    overflow: hidden;
  }
  .card--back  { left: 519px; top: 351px; z-index: 1; }
  .card--front { left: 102px; top: 51px;  z-index: 2; }

  .card__wave { position: absolute; left: 0; top: 0; width: 100%; height: 100%; }

  .brand {
    position: absolute;
    display: flex;
    align-items: center;
    gap: 14px;
  }
  .brand__mark { background: var(--yellow); flex: none; }
  .brand__name {
    color: var(--green);
    font-weight: 700;
    text-transform: uppercase;
    line-height: 1.05;
    letter-spacing: 0.5px;
  }
  .card--front .brand { left: 46px; top: 40px; }
  .card--front .brand__mark { width: 58px; height: 58px; }
  .card--front .brand__name { font-size: 25px; }

  .card--back .brand { left: 0; right: 0; top: 118px; justify-content: center; }
  .card--back .brand__mark { width: 80px; height: 80px; }
  .card--back .brand__name { font-size: 32px; }

  .person { position: absolute; left: 46px; top: 176px; }
  .person__name { color: var(--green); font-weight: 700; font-size: 20px; line-height: 1.2; }
  .person__role { color: var(--yellow); font-weight: 600; font-size: 16px; line-height: 1.4; }

  .contact {
    position: absolute;
    left: 376px;
    right: 12px;
    top: 236px;
    list-style: none;
    font-family: "Arimo", Arial, sans-serif;
    color: var(--white);
    font-size: 16px;
  }
  .contact__item { display: flex; align-items: center; gap: 7px; height: 27.5px; white-space: nowrap; }
  .contact__icon { width: 13px; height: 13px; flex: none; }
  .contact__icon--social { background: var(--white); width: 12px; height: 12px; }
</style>
</head>
<body>

  <section class="card card--back" aria-label="Business card back">
    <div class="brand">
      <span class="brand__mark"></span>
      <span class="brand__name">Harbourlight<br>Campus<br>Lodgings</span>
    </div>
  </section>

  <section class="card card--front" aria-label="Business card front">
    <svg class="card__wave" viewBox="0 0 597 341" preserveAspectRatio="none" aria-hidden="true">
      <path d="M0 274 C120 318 220 250 330 214 C430 184 520 186 597 196 L597 341 L0 341 Z" fill="var(--green)"/>
      <path d="M0 238 C90 262 170 262 260 230 C360 196 470 172 597 186 C480 180 380 200 280 240 C180 280 80 284 0 258 Z" fill="var(--yellow)"/>
    </svg>

    <div class="brand">
      <span class="brand__mark"></span>
      <span class="brand__name">Harbourlight<br>Campus<br>Lodgings</span>
    </div>

    <div class="person">
      <p class="person__name">Employee Name</p>
      <p class="person__role">Position</p>
    </div>

    <ul class="contact">
      <li class="contact__item">
        <svg class="contact__icon" viewBox="0 0 16 16" aria-hidden="true">
          <path d="M3.5 1.5 L6 1 L7.5 4.5 L5.8 5.8 C6.6 7.6 8.2 9.3 10.2 10.2 L11.5 8.5 L15 10 L14.5 12.5 C14.2 14 12.8 15 11.3 14.8 C6 14 2 10 1.2 4.7 C1 3.2 2 1.8 3.5 1.5 Z" fill="var(--white)"/>
        </svg>
        <span>123-456-7890</span>
      </li>
      <li class="contact__item">
        <svg class="contact__icon" viewBox="0 0 16 16" aria-hidden="true">
          <rect x="1" y="3" width="14" height="10" fill="var(--white)"/>
          <path d="M1 3.5 L8 9 L15 3.5" fill="none" stroke="var(--green)" stroke-width="1.3"/>
        </svg>
        <span>info@harbourlight.com</span>
      </li>
      <li class="contact__item">
        <span class="contact__icon contact__icon--social"></span>
        <span>/harbourlight</span>
      </li>
    </ul>
  </section>

</body>
</html>
```